Personal Vistrano Banner

I am creating a personal brand for myself. I want a vistrano banner that inspires and motivates people to reach their epic awesomeness. I am creating and designing my personal brand. It can be a background with words on a scenery a picture or 3d graphic. If someone looked at it, they should say it is aggressively epic and motivating. It should be dramatic and bold.
My personal goal is to help as many people reach financial freedom as possible, and challenge and break their own limiting beliefs. This personal brand will be integrated into my zomblat, quorVex, and professional vistrano fanpage (in addition to personal page). My goals are to open up a school for the underpriveleged children, develop my network marketing company team, and become a billionaire in the process. I want to attract people to me that really identify with doing what most think is impossible in terms of personal growth, impact to the world and financial wealth.
Updates

I have updated my brief with more background, and added a new comment to the discussion section to give you more to work with.

Reason: To give designers more time and to create a second and third place prize.

Reason: I am giving designers time to submit more designs

Target Market(s)

business professionals, and people with an entrepreneurial spirit.

Industry/Entity Type

Financial

Requirements
Must have
• It must be the exact dimensions required for vistrano banners. It should not be bigger or smaller. exact!!!

```html
<!DOCTYPE html>
<html lang="en">
<head>
<meta charset="utf-8">
<title>Reach Your Epic Awesomeness — Vistrano Banner</title>
<link rel="stylesheet" href="https://fonts.googleapis.com/css2?family=Russo+One&display=swap">
<style>
  :root {
    --sky-top: #2e2f6e;
    --sky-mid: #7a4a86;
    --sky-glow: #e0566a;
    --sun: #ffd9a0;
    --floor: #8a8a8a;
    --floor-dark: #5e5e5e;
    --cloud: #e4e4e6;
    --ink-dark: #2b2b2b;
    --ink-dark-side: #151515;
    --epic-red: #c8120f;
    --epic-side: #6e0504;
    --stone: #a9a9a9;
    --stone-side: #6f6f6f;
  }
  html, body {
    margin: 0;
    padding: 0;
    overflow: hidden;
    background: #ffffff;
  }
  .banner {
    position: relative;
    width: 1200px;
    height: 444px;
    overflow: hidden;
    font-family: "Russo One", "Arial Black", sans-serif;
    text-transform: uppercase;
  }
  .scenery {
    position: absolute;
    inset: 0;
    width: 1200px;
    height: 444px;
  }
  .headline {
    position: absolute;
    margin: 0;
    line-height: 1;
    white-space: nowrap;
    transform-origin: left top;
  }
  .headline--lead {
    left: 44px;
    top: 116px;
    font-size: 66px;
    letter-spacing: 2px;
    color: var(--ink-dark);
    transform: scaleY(1.25);
    text-shadow:
      1px 1px 0 var(--ink-dark-side),
      2px 2px 0 var(--ink-dark-side),
      3px 3px 0 var(--ink-dark-side),
      4px 4px 0 var(--ink-dark-side);
  }
  .headline--epic {
    left: 560px;
    top: 40px;
    font-size: 176px;
    letter-spacing: 4px;
    color: var(--epic-red);
    transform: scaleY(1.05);
    text-shadow:
      2px 2px 0 var(--epic-side),
      4px 4px 0 var(--epic-side),
      6px 6px 0 var(--epic-side),
      8px 8px 0 var(--epic-side),
      10px 10px 0 var(--epic-side),
      12px 12px 0 var(--epic-side);
  }
  .headline--main {
    left: 34px;
    top: 190px;
    font-size: 132px;
    letter-spacing: 1px;
    color: var(--stone);
    transform: scaleY(1.15);
    text-shadow:
      2px 2px 0 var(--stone-side),
      4px 4px 0 var(--stone-side),
      6px 6px 0 var(--stone-side),
      8px 8px 0 var(--stone-side),
      10px 10px 0 var(--stone-side);
  }
</style>
</head>
<body>
  <div class="banner">
    <svg class="scenery" viewBox="0 0 1200 444" role="img" aria-label="Dramatic sunset sky over a sea of clouds with a grey stone platform">
      <defs>
        <linearGradient id="skyGradient" x1="0" y1="0" x2="1" y2="0.4">
          <stop offset="0" stop-color="var(--sky-top)"/>
          <stop offset="0.45" stop-color="var(--sky-mid)"/>
          <stop offset="1" stop-color="var(--sky-glow)"/>
        </linearGradient>
        <radialGradient id="sunGlow" cx="1045" cy="140" r="260" gradientUnits="userSpaceOnUse">
          <stop offset="0" stop-color="var(--sun)" stop-opacity="0.95"/>
          <stop offset="0.35" stop-color="#f08a6e" stop-opacity="0.55"/>
          <stop offset="1" stop-color="var(--sky-glow)" stop-opacity="0"/>
        </radialGradient>
        <linearGradient id="floorGradient" x1="0" y1="0" x2="0" y2="1">
          <stop offset="0" stop-color="var(--floor)"/>
          <stop offset="1" stop-color="var(--floor-dark)"/>
        </linearGradient>
        <radialGradient id="cloudSoft" cx="0.5" cy="0.5" r="0.5">
          <stop offset="0" stop-color="var(--cloud)" stop-opacity="0.9"/>
          <stop offset="1" stop-color="var(--cloud)" stop-opacity="0"/>
        </radialGradient>
      </defs>
      <rect class="sky" width="1200" height="444" fill="url(#skyGradient)"/>
      <rect class="sun-glow" width="1200" height="444" fill="url(#sunGlow)"/>
      <polygon class="platform" points="0,300 1200,330 1200,444 0,444" fill="url(#floorGradient)"/>
      <ellipse class="cloud" cx="60" cy="160" rx="120" ry="60" fill="url(#cloudSoft)"/>
      <ellipse class="cloud" cx="1150" cy="250" rx="110" ry="90" fill="url(#cloudSoft)"/>
      <ellipse class="cloud" cx="650" cy="350" rx="420" ry="45" fill="url(#cloudSoft)"/>
      <ellipse class="cloud" cx="1000" cy="360" rx="240" ry="40" fill="url(#cloudSoft)"/>
    </svg>

    <h1 class="headline headline--epic">Epic</h1>
    <p class="headline headline--lead">Reach your</p>
    <p class="headline headline--main">Awesomeness</p>
  </div>
</body>
</html>
```